Website - TRSC

Having reviewed the designs received so far, no one design is meeting the client’s needs. The client has identified desirable elements from the designs submitted, which we want to see brought together.
Header
It is important that the logo is given space – ie is not overlayed on an image, nor with a short fade into an image. A gradual fade into the header image is acceptable.
Background
While an image background is acceptable, this should only be visible on the left and right borders, it should not be used underneath the main content area.
Main menu
The main menu should be a cohesive bar across the page – not separate buttons. Buttons that are connected together within a bar are acceptable. Menu items should be separated using a pipe ( | ), or by being framed (as long as the framing sits within a bar). Menu item should change colour to indicate the page you are on.
Left Hand Boxes
There should be consistency in colouring through these. It is acceptable to use one colour for the heading , and another for the content area. It is not acceptable for each box to have a different scheme. This applies to the right hand feature boxes as well.
Colouring
We want to keep this simple. Please use colours from the logo, feel free to add complimentary colours but keep the palette limited. If shading is used with any of the colours be careful to not move it too far from the original colour. The yellow does not look good with too much of a grey shade.
Feature Boxes
The two feature boxes on the home page (Browse Homes and Local Knowledge) need to stand out. An option is to ensure that the associated link button uses one of the brighter colours in the palette.
_____________________________________________________
Note: I have attached the newly design logo to the brief. It is important that colours from the logo are used on the design. Blue denotes water and the yellow denotes sand and sun.
I'd like to see the feel of the logo reflected in the site.
______________________________________________
Tui Crib and Seaside Cottages is rebuilding its website – www.tuicribandseasidecottages.co.nz.
We require the design of two pages:
• Home
• House detail page (pgs 3-5 of the attachment).
We have specified a layout for the site (attached).
The contextual information below provides the feeling the site needs to convey.
If further information is required please contact us.
CONTEXT/BACKGROUND
Tui Crib and Seaside Cottages (TRSC) has been in business now for over 11 years and is due for a facelift. We have about 40 – 60 houses available during the peak summer period – about 50% are permanent holiday homes, the balance are local family homes being rented out while they are away on holiday.
We are currently located in Marram Sands – but with the national name have the ability and goal to expand into other areas of New Zealand – so any logo etc has to have the ability to represent other holiday destinations within NZ. Bear in mind that our primary location is Marram at the moment.
Our key market is families going on holiday – looking for a holiday home to book (currently an Marram Sands holiday)
Secondary market is couples or mature groups looking at having some R&R or business groups having some team building/ management meetings away from the busy office surroundings.
We manage ALL the properties so are a great source of information on what holiday home is best suited to each family and “things to do” in the area – i.e. other activities.
Our main focus is to be the best “holiday home” - accommodation provider in whatever location TRSC is representing. We want to be seen as having a good supply of great homes, providing a great service as well as being a good source of local knowledge.
We want to be seen as PROFESSIONALS in the holiday rental business (from occupants and owners).
TRUST – we want people to be able to trust us by listing their property with us (owners) and confidently booking accommodation through us (occupants).
TAGLINE SUGGESTIONS
Key motif – “TRSC, your door to a fine escape!” The “key”, of course is a double play on the house key you get. But it is also extendible to other aspect of the experience we offer. For example the phrase: “getting the key to the city” is applicable to us – we give them the key to Marram…(or whatever location we are marketing in the future). Potentially we may consider promotional merchandise around this, eg promo key rings etc.
Some key words/phrases that our business represents are:
• ‘Our place is your place’
• Connect – connecting families to holiday homes and the area – at the moment only Marram.
• Local – local people looking after your needs – “our place is your place – so make yourself at home!”
• Link – we are the link to a real kiwi holiday experience.
• Holiday - R&R – rest and recreation
More specific to Marram:
• Safe Natural playground – beach, bush, fishing, outdoor activities – creating real family memories.
Website:
• Need to focus on the Local and Personal property management factors in website to differentiate us from other nationwide listing sites – contact us and we can help you find the right accommodation and save you time
• Play on the HOLIDAYMAKER experience more, including giving prominence to visitor deals, become a local etc, differentiating us from other local holiday home rental businesses.
• Real – real people, real places, real experiences.
• User friendly, informative, professional with a personal touch/feel, to encourage the holiday feeling.
Having reviewed the designs received so far, no one design is meetingthe client’s needs. The client has identified desirable elements from thedesigns submitted, which we want to see brought together.
Header
It is important that the logo is given space – ie is not overlayed on animage, nor with a short fade into an image. A gradual fade into the headerimage is acceptable.
Background
While an image background is acceptable, this should only be visible onthe left and right borders, it should not be used underneath the main contentarea.
Main menu
The main menu should be a cohesive bar across the page – not separatebuttons. Buttons that are connected together within a bar are acceptable.Menu items should be separated using a pipe ( | ), or by being framed (as longas the framing sits within a bar). Menu item should change colour to indicatethe page you are on.
Left Hand Boxes
There should be consistency in colouring through these. It isacceptable to use one colour for the heading , and another for the contentarea. It is not acceptable for each box to have a different scheme. Thisapplies to the right hand feature boxes as well.
Colouring
We want to keep this simple. Please use colours from the logo,feel free to add complimentary colours but keep the palette limited. Ifshading is used with any of the colours be careful to not move it too far fromthe original colour. The yellow does not look good with too much of agrey shade.
Feature Boxes
The two feature boxes on the home page (Browse Homes and LocalKnowledge) need to stand out. An option is to ensure that the associated linkbutton uses one of the brighter colours in the palette.

```html
<!DOCTYPE html>
<html lang="en">
<head>
<meta charset="utf-8">
<title>Tui Crib and Seaside Cottages – Home</title>
<link rel="stylesheet" href="https://fonts.googleapis.com/css2?family=Arimo:ital,wght@0,400;0,700;1,700&family=Open+Sans:wght@300;400&family=Ubuntu:wght@400;500&display=swap">
<style>
:root{
  --sand:#dcd3c0;
  --sky-top:#0f7fb4;
  --sky-mid:#5cc3e8;
  --sky-light:#bfe8f6;
  --cyan:#1eb8f0;
  --blue:#0a78bb;
  --deep-blue:#06568c;
  --menu-text:#0d2b40;
  --label-yellow:#ffe65c;
  --lime:#9cd23a;
  --lime-dark:#6aa51f;
  --green:#2fa84a;
  --ink:#111;
  --teal-heading:#1b7f8c;
  --white:#fff;
}
*{box-sizing:border-box;margin:0;padding:0}
html,body{width:902px;height:1200px;overflow:hidden;background:var(--sand)}
body{font-family:"Arimo",Arial,sans-serif;color:var(--ink)}
.page{position:relative;width:902px;height:1200px;overflow:hidden;background:var(--sand)}
.abs{position:absolute}

/* header */
.header-bg{left:0;top:0;width:902px;height:280px;
  background:linear-gradient(180deg,var(--sky-top) 0%,var(--sky-mid) 45%,var(--sky-light) 72%,var(--sand) 100%)}
.brand{left:19px;top:84px;width:270px;color:var(--white);font-family:"Open Sans",sans-serif;font-weight:400;font-size:24px;line-height:29px}
.brand .place{display:block;font-size:21px;margin-top:4px;margin-left:26px}
.hero{left:316px;top:19px;width:573px;height:223px;border-radius:10px;overflow:hidden;
  background:linear-gradient(180deg,#8ec9ea 0%,#cfe3ea 35%,#b08a6a 60%,#5d7e4a 80%,#3f8aa8 100%);
  border:2px solid #e9f6fb}
.hero-band{position:absolute;left:0;bottom:0;width:100%;height:50px;background:rgba(20,30,40,.72)}
.hero-tagline{position:absolute;left:70px;bottom:8px;color:var(--white);font-family:"Ubuntu",sans-serif;font-size:25px;white-space:nowrap}
.hero-dots{position:absolute;right:28px;bottom:16px;display:flex;gap:4px}
.hero-dots span{width:13px;height:13px;border-radius:50%;background:var(--cyan);border:2px solid var(--white)}
.hero-dots span:first-child{background:transparent}

/* main menu */
.main-menu{left:10px;top:278px;width:881px;height:45px;border-radius:12px;
  background:linear-gradient(180deg,#7fdcff 0%,var(--cyan) 45%,#0e9fdc 100%);border:2px solid #d7f3ff;
  display:flex;align-items:center;justify-content:space-between;padding:0 40px 0 44px;
  font-family:"Ubuntu",sans-serif;font-size:15px;color:var(--menu-text);white-space:nowrap}
.main-menu a{color:inherit;text-decoration:none;white-space:nowrap}
.main-menu a.current{color:var(--white)}
.main-menu .pipe{font-weight:500}

/* left boxes */
.side-box{left:9px;width:244px;border-radius:10px;overflow:hidden;
  background:linear-gradient(180deg,var(--cyan) 0%,var(--blue) 100%);border:2px solid #c9eefc;color:var(--white)}
.side-title{font-family:"Open Sans",sans-serif;font-weight:300;font-size:22px;padding:7px 13px 0}
.field-label{position:absolute;left:26px;color:var(--label-yellow);font-size:13px}
.field{position:absolute;height:14px;background:var(--white);border:1px solid #9fb7c4;font-size:8px;color:#999;padding-left:3px;line-height:12px}
.field.select::after{content:"";position:absolute;right:4px;top:4px;border:4px solid transparent;border-top-color:#222}
.btn-lime{position:absolute;height:22px;border-radius:6px;background:linear-gradient(180deg,#d5f27a,var(--lime) 50%,var(--lime-dark));
  color:#1d2c08;font-size:14px;font-weight:700;display:flex;align-items:center;justify-content:center;gap:6px;font-family:"Arimo",sans-serif}
.btn-lime .arrows{font-size:10px}
.link-white{position:absolute;color:var(--white);font-size:12px;text-decoration:underline}
.box-text{position:absolute;color:var(--white);font-size:10px;line-height:13px}

/* content */
.welcome{left:267px;top:340px;width:441px;font-family:"Open Sans",sans-serif;font-weight:400;font-size:16px;color:#222;border-bottom:1px solid #b9ad95;padding-bottom:5px;white-space:nowrap}
.welcome span{color:var(--teal-heading);font-size:21px;font-weight:400}
.copy{position:absolute;font-size:10px;line-height:16px;color:#111}
.help-box{left:723px;top:340px;width:168px;height:194px;border-radius:8px;background:linear-gradient(180deg,var(--cyan),#0fa0e0);border:2px solid #c9eefc}
.help-tab{left:721px;top:358px;width:121px;height:35px;background:linear-gradient(180deg,#4cc25a,var(--green));color:var(--white);
  font-family:"Open Sans",sans-serif;font-size:20px;padding:3px 0 0 24px}
.help-q{left:730px;top:405px;width:160px;font-size:11px;font-weight:700;font-style:italic;line-height:13px}
.help-sub{left:735px;top:437px;width:150px;font-size:10px;line-height:13px}
.help-call{left:740px;top:470px;color:var(--white);font-weight:700;font-style:italic;font-size:16px;line-height:21px;white-space:nowrap}
.callout{left:267px;top:762px;width:630px;font-family:"Arimo",sans-serif;font-weight:700;font-style:italic;font-size:17.5px;line-height:21px;letter-spacing:.3px;color:#0b0b0b;text-transform:uppercase}
.callout a{color:#1aa0dd;text-decoration:underline}
.feature{top:810px;width:307px;height:178px;border-radius:8px}
.feature-browse{left:262px;background:linear-gradient(135deg,#6a5a4e 0%,#3b2f2a 45%,#2f6fb0 75%,#5ba0d8 100%)}
.feature-local{left:584px;background:linear-gradient(180deg,#4fa6e0 0%,#8fd0ef 45%,#2a7a3a 70%,#d8cda6 100%)}
.feature-btn{top:969px;width:245px;height:45px;border-radius:9px;background:linear-gradient(180deg,#7fdcff,var(--cyan) 55%,#0e9fdc);
  border:2px solid #e3f7ff;color:var(--menu-text);font-family:"Ubuntu",sans-serif;font-size:20px;display:flex;align-items:center;justify-content:center;text-decoration:none;white-space:nowrap}

/* social & share */
.like{left:9px;top:1074px;width:45px;height:19px;border:1px solid #9aa6b8;border-radius:3px;background:#eef1f6;font-size:10px;color:#3b4a66;display:flex;align-items:center;justify-content:center}
.share{left:9px;top:1098px;display:flex;align-items:center;gap:10px;font-size:11px;color:#222}
.share .tile{width:26px;height:24px;border-radius:4px;border:1px solid #5d7894;background:#e6eef5}
.social-name{color:var(--white);font-size:11px;font-family:"Arimo",sans-serif}

/* footer */
.footer{left:9px;top:1145px;width:882px;height:44px;border-radius:12px;background:linear-gradient(180deg,#7fdcff,var(--cyan) 50%,#0e9fdc);
  border:2px solid #d7f3ff;text-align:center;font-size:9.5px;line-height:15px;color:#0b1e2b;padding-top:6px}
</style>
</head>
<body>
<div class="page">

  <div class="abs header-bg" role="img" aria-label="Sea and sky backdrop fading into sand"></div>
  <div class="abs brand">Tui Crib &amp; Seaside Cottages<span class="place">Marram Sands</span></div>

  <div class="abs hero" role="img" aria-label="Photo of a sunny holiday home with pool and lawn">
    <div class="hero-band"></div>
    <div class="hero-tagline">TRSC, your door to a fine escape!</div>
    <div class="hero-dots"><span></span><span></span><span></span><span></span><span></span></div>
  </div>

  <nav class="abs main-menu">
    <a class="current" href="#">Home</a><span class="pipe">|</span>
    <a href="#">Browse Homes</a><span class="pipe">|</span>
    <a href="#">Packages</a><span class="pipe">|</span>
    <a href="#">Local Knowelgdes</a><span class="pipe">|</span>
    <a href="#">About Us</a><span class="pipe">|</span>
    <a href="#">Contact Us</a><span class="pipe">|</span>
    <a href="#">List Your Home</a>
  </nav>

  <!-- Quick search -->
  <section class="abs side-box" style="top:338px;height:254px">
    <h2 class="side-title">Quick Search</h2>
  </section>
  <div class="field-label" style="top:386px">No. of Guest</div>
  <div class="field select" style="left:26px;top:408px;width:212px">Feb 2011</div>
  <div class="field-label" style="top:434px">Nightly Rate</div>
  <div class="field select" style="left:26px;top:454px;width:85px">Feb 2011</div>
  <div class="field-label" style="left:123px;top:452px">TO</div>
  <div class="field select" style="left:151px;top:454px;width:87px">$200</div>
  <div class="field-label" style="top:484px">Keywords</div>
  <div class="field" style="left:26px;top:505px;width:212px">Beach access</div>
  <div class="btn-lime" style="left:26px;top:537px;width:72px">enter <span class="arrows">»</span></div>
  <a class="link-white" href="#" style="left:110px;top:540px">Advanced Search</a>

  <!-- Keep in touch -->
  <section class="abs side-box" style="top:601px;height:267px">
    <h2 class="side-title">Keep in Touch</h2>
  </section>
  <div class="box-text" style="left:27px;top:651px;width:220px;font-size:10px;font-weight:700;color:#fff">Newsletter with Deals &amp; Local Knowledge To Your Inbox</div>
  <div class="field-label" style="left:27px;top:690px">Name</div>
  <div class="field" style="left:71px;top:690px;width:167px"></div>
  <div class="field-label" style="left:27px;top:721px">Email</div>
  <div class="field" style="left:71px;top:721px;width:167px"></div>
  <div class="btn-lime" style="left:156px;top:751px;width:82px">submit <span class="arrows">»</span></div>
  <div class="abs" style="left:11px;top:793px;width:240px;height:1px;background:#7fd0f2"></div>
  <div class="abs" style="left:25px;top:808px;color:#fff;font-family:'Open Sans',sans-serif;font-size:20px;line-height:20px">Find us<br><span style="margin-left:16px">On</span></div>
  <div class="abs social-name" style="left:118px;top:826px">Friendbook</div>
  <div class="abs social-name" style="left:187px;top:826px">Chirper</div>

  <!-- Deal -->
  <section class="abs side-box" style="top:879px;height:187px">
    <h2 class="side-title">Deal</h2>
  </section>
  <div class="abs" role="img" aria-label="Photo of a cosy bedroom" style="left:25px;top:929px;width:75px;height:83px;background:linear-gradient(135deg,#e3b06a,#7a4a26)"></div>
  <div class="box-text" style="left:107px;top:925px;width:144px;font-size:9.5px;line-height:13px">Lorem ipsum onsectetuer adipiscing elit, sed diam nonummy nibh euismod tincidunt ut laoreet lore magna aliquam erat volutpat. Ut wisi enim ad minim veniam, quis</div>
  <div class="abs" style="left:11px;top:1027px;width:240px;height:37px;background:var(--deep-blue)"></div>
  <div class="abs" style="left:32px;top:1036px;color:#fff;font-weight:700;font-style:italic;font-size:13px">$1955.55</div>
  <div class="btn-lime" style="left:167px;top:1033px;width:71px">view <span class="arrows">»</span></div>

  <div class="abs like">Like</div>
  <div class="abs share">Share This
    <span class="tile"></span><span class="tile"></span><span class="tile"></span><span class="tile"></span>
  </div>

  <!-- Content -->
  <h1 class="abs welcome">Welcome to <span>Tui Crib &amp; Seaside Cottages</span></h1>
  <p class="copy" style="left:267px;top:384px;width:443px">Lorem ipsum onsectetuer adipiscing elit, sed diam nonummy nibh euismod tincidunt ut laoreet dolore magna aliquam erat volutpat. Ut wisi enim ad minim veniam, quis nostrud exerci tation ullamcorper suscipit lobortis nisl ut aliquip ex ea commodo consequat.</p>
  <p class="copy" style="left:267px;top:450px;width:443px">Lorem ipsum onsectetuer adipiscing elit, sed diam nonummy nibh euismod tincidunt ut laoreet dolore magna aliquam erat volutpat. Ut wisi enim ad minim veniam, quis nostrud exerci tation ullamcorper suscipit lobortis nisl ut aliquip ex ea commodo consequat.Lorem ipsum onsectetuer adipiscing elit, sed diam nonummy nibh euismod tincidunt ut laoreet dolore magna aliquam erat volutpat. Ut wisi enim ad minim veniam, quis nostrud exerci tation ullamcorper suscipit lobortis nisl ut aliquip ex ea commodo</p>
  <p class="copy" style="left:269px;top:562px;width:622px">Lorem ipsum onsectetuer adipiscing elit, sed diam nonummy nibh euismod tincidunt ut laoreet dolore magna aliquam erat volutpat. Ut wisi enim ad minim veniam, quis nostrud exerci tation ullamcorper suscipit lobortis nisl ut aliquip ex ea commodo consequat.</p>
  <p class="copy" style="left:269px;top:627px;width:622px">Lorem ipsum onsectetuer adipiscing elit, sed diam nonummy nibh euismod tincidunt ut laoreet dolore magna aliquam erat volutpat. Ut wisi enim ad minim veniam, quis nostrud exerci tation ullamcorper suscipit lobortis nisl ut aliquip ex ea commodo consequat.Lorem ipsum onsectetuer adipiscing elit, sed diam nonummy nibh euismod tincidunt ut laoreet dolore magna aliquam erat volutpat. Ut wisi enim ad minim veniam, quis nostrud exerci tation ullamcorper suscipit lobortis nisl ut aliquip ex ea commodo consequat.</p>

  <!-- Help -->
  <aside class="abs help-box"></aside>
  <div class="abs help-tab">Help
    <svg width="12" height="12" viewBox="0 0 12 12" style="position:absolute;right:12px;top:12px" aria-hidden="true"><path d="M1 3v8h8M5 1h6v6M11 1L5 7" fill="none" stroke="#fff" stroke-width="1.4"/></svg>
  </div>
  <div class="abs help-q">CAN'T FIND WHAT YOU'RE LOOKING FOR?</div>
  <div class="abs help-sub">Contact Us For A Personal Property Search</div>
  <div class="abs help-call">&nbsp;Call Us At<br>+64-27-555-0142</div>

  <!-- Callout and features -->
  <p class="abs callout">Just can't find what you're looking for? <a href="#">Contact us</a> for a personal property search.</p>
  <div class="abs feature feature-browse" role="img" aria-label="Photo of a dining room beside a sea view window"></div>
  <div class="abs feature feature-local" role="img" aria-label="Photo of a catamaran on a palm-fringed beach"></div>
  <a class="abs feature-btn" href="#" style="left:292px">BROWSE HOMES</a>
  <a class="abs feature-btn" href="#" style="left:614px">LOCAL KNOWLEDGE</a>

  <footer class="abs footer">
    Terms &amp; Conditions &nbsp; | &nbsp; Privacy Policy &nbsp; | &nbsp; Contact Us &nbsp; | &nbsp; List Your HomeMy<br>© 2011, All Rights Reserved,
  </footer>
</div>
</body>
</html>
```